Commercial Cleaning Company Website Design

We are working with Harbor Tidy Squad. They are a commercial cleaning company that needs a new website design.

Some sites to use for inspiration:

https://www.velmoxa.com
https://glint-panewashing.com
https://tidykelps.net
https://warmnestdwell.com
https://www.thescrubbingcouncil.com
https://www.pennybroom.com

Thank you for taking the time to consider designing a website for us. We are web developers based in Stockton and Los Angeles, CA, USA. Most of our projects go through the same process. Understanding this process may help you win a project with us. We custom-code all of our websites in-house. We don’t have any requirements as to what tools you use for your design, but we prefer Figma files. For any design that we label as four-stars, we send it to the client for review. The client picks the final design they want us to use. Once we complete this process, we will continue to show additional clients all the four-star sites and purchase them later. Your designs will have multiple chances to sell. For better chances of success, we ask that you follow these guidelines.

IMAGES:
If you use any images or icons in the design, we ask that you have a link to the asset so we can purchase the image/icon. Most of the designs we submit do not have the customer’s images on them unless they have some great images. Be creative; show us the feeling you are trying to portray with your image choices. Use any royalty-free site you choose. We subscribe to Vorlan and mainly use their images, but we can purchase images outside of Vorlan.

PLEASE NOTE: we will not submit designs to clients with watermarks on the images.

FONTS:
We ask that you identify the fonts used in the design. This can be done in a message if you want. We typically use Google Fonts and Vorlan Fonts.

CONTENT:
We're always open to different content and ideas. We often submit designs with stock images so the client can see our vision. We typically take pictures after the website launch to use their images with our vision. Lorem Ipsum is fine for paragraphs, but we ask that you write the headers in correct English. We want to be able to show the vision and identify the sections of the website.

INSPIRATION:
We typically add a couple of links in the brief of websites we like to help you get started in your design.

REVISIONS:
We do not often ask for revisions of the designs unless we see something in the design that may not appeal to the client. If there are slight changes that we want to make, we do that in the development process.

FEEDBACK:
We rarely give feedback on designs during the design process. We are working on many website projects and do not have the time to provide feedback. We usually respond if your request is well thought out and asks specific questions, but a note asking “feedback, please” usually goes unanswered.

```html
<!DOCTYPE html>
<html lang="en">
<head>
<meta charset="utf-8">
<title>Harbor Tidy Squad — Commercial Cleaning</title>
<link rel="stylesheet" href="https://fonts.googleapis.com/css2?family=Poppins:wght@400;500;600;700&display=swap">
<style>
:root{
  --blue:#1b47c2;
  --blue-dark:#163aa3;
  --red:#ee2b1f;
  --yellow:#f7c21a;
  --ink:#222630;
  --muted:#5d6270;
  --pale:#eef2fb;
  --white:#ffffff;
  --line:#d7dbe4;
}
*{box-sizing:border-box;margin:0;padding:0}
html,body{width:1200px;height:4545px;overflow:hidden}
body{font-family:"Poppins",sans-serif;color:var(--ink);background:var(--white);position:relative;font-size:11px}
.wrap{width:975px;margin:0 auto;position:relative}
a{color:inherit;text-decoration:none}
.btn{display:inline-block;background:var(--yellow);color:var(--blue-dark);font-weight:600;font-size:10px;text-transform:uppercase;border-radius:4px;padding:7px 16px}
.h2{font-size:27px;font-weight:600;color:var(--blue);text-align:center}
.lead{font-size:10.5px;color:var(--muted);text-align:center;line-height:1.6;max-width:560px;margin:8px auto 0}
.ph{display:block}

/* nav */
.nav{height:65px}
.nav .wrap{display:flex;align-items:center;height:65px;justify-content:space-between}
.brand{display:flex;align-items:center;gap:8px;font-weight:600;color:var(--blue);font-size:15px;letter-spacing:1px}
.brand i{width:12px;height:12px;background:var(--red);border-radius:50%;display:block}
.menu{display:flex;gap:32px;align-items:center;font-size:11px;font-weight:500}
.menu .active{color:var(--blue);border-bottom:2px solid var(--blue);padding-bottom:3px}
.menu .btn{padding:6px 18px}

/* hero */
.hero{height:563px;position:relative;background:linear-gradient(90deg,#f4f4f4 0%,#e9e9e9 55%,#c9c3bd 100%)}
.hero .wrap{padding-top:170px}
.hero h1{font-size:41px;line-height:1.15;color:var(--blue);font-weight:600}
.hero p{font-size:10.5px;color:#444;width:440px;margin-top:10px;line-height:1.5}
.search{margin-top:30px;width:568px;height:44px;background:var(--white);border-radius:4px;display:flex;align-items:center;box-shadow:0 4px 14px rgba(0,0,0,.08)}
.search span{flex:1;display:flex;align-items:center;justify-content:center;gap:6px;font-size:9.5px;font-weight:500;text-transform:uppercase}
.search .btn{height:44px;border-radius:0 4px 4px 0;display:flex;align-items:center;padding:0 24px}
.stats{position:absolute;left:113px;top:515px;width:975px;height:93px;background:var(--red);border-radius:4px;display:flex;align-items:center;color:var(--white)}
.stat{flex:1;text-align:center;border-right:1px solid rgba(255,255,255,.45)}
.stat:last-child{border:0}
.stat b{display:block;font-size:29px;font-weight:600;line-height:1.1}
.stat small{font-size:9.5px}

/* excellence */
.excel{height:420px;padding-top:115px}
.excel .wrap{display:flex;gap:100px}
.excel .photo{width:432px;height:268px;border-radius:6px 6px 26px 6px;background:linear-gradient(135deg,#6b5845,#2f3b55 60%,#c9a640)}
.badge{position:absolute;left:392px;top:-10px;width:100px;height:100px;border-radius:50%;background:var(--blue);border:4px solid var(--white);color:var(--white);text-align:center;padding-top:18px;box-shadow:0 4px 10px rgba(0,0,0,.2)}
.badge b{font-size:27px;font-weight:600;display:block;line-height:1}
.badge small{font-size:9px;line-height:1.1;display:block}
.excel h2{font-size:27px;color:var(--blue);font-weight:600;margin-top:5px}
.excel p{font-size:10px;color:var(--muted);line-height:1.6;margin-top:8px;width:400px}
.ticks{list-style:none;margin-top:14px}
.ticks li{display:flex;gap:8px;font-size:10px;font-weight:500;margin-bottom:10px;width:340px;line-height:1.45}
.ticks svg{flex:none;margin-top:2px}
.excel .btn{margin-top:10px}

/* services */
.services{height:425px}
.cards{display:flex;gap:19px;margin-top:20px}
.card{width:312px;height:339px;border-radius:6px;overflow:hidden;box-shadow:0 6px 16px rgba(0,0,0,.1);position:relative;background:var(--white)}
.card .ph{height:291px;background:linear-gradient(160deg,#cfd6dd,#6c7a86 60%,#2b3440)}
.card .label{height:48px;display:flex;align-items:center;gap:14px;padding:0 19px;font-size:13px;font-weight:500}
.card.feature .ph{height:339px}
.card.feature .over{position:absolute;left:0;bottom:0;width:100%;height:120px;background:var(--blue);color:var(--white);padding:16px 19px}
.over h3{font-size:13px;font-weight:600}
.over p{font-size:9.5px;line-height:1.5;margin-top:4px}
.over a{font-size:9.5px;display:inline-flex;gap:6px;margin-top:6px;align-items:center}
.center{text-align:center;margin-top:30px}

/* how */
.how{height:380px;background:var(--pale);padding-top:40px}
.steps{display:flex;justify-content:space-between;margin-top:38px;position:relative}
.step{width:280px;text-align:center}
.ring{width:100px;height:100px;border-radius:50%;background:var(--white);border:1.5px solid #8ea3da;margin:0 auto;display:flex;align-items:center;justify-content:center}
.step h3{font-size:13px;font-weight:600;margin-top:18px}
.step p{font-size:9.5px;color:var(--muted);line-height:1.55;margin-top:6px}
.dash{position:absolute;top:0;left:0}

/* why */
.why{height:420px;padding-top:75px}
.why .wrap{display:flex;justify-content:space-between}
.why h2{font-size:27px;color:var(--blue);font-weight:600}
.why .intro{font-size:10px;color:var(--muted);line-height:1.6;width:445px;margin-top:8px}
.feats{display:grid;grid-template-columns:250px 220px;gap:22px 0;margin-top:18px}
.feat{display:flex;gap:8px}
.feat b{font-size:10.5px;font-weight:600;display:block}
.feat span{font-size:9.5px;color:var(--muted);line-height:1.4;display:block;margin-top:2px}
.why .photo{width:476px;height:296px;border-radius:6px 6px 26px 6px;background:linear-gradient(135deg,#e8ecef,#9aa6ae 55%,#d9c255);margin-top:-25px}

/* testimonials */
.testi{height:377px;background:var(--blue);padding-top:38px;position:relative}
.testi .h2{color:var(--white)}
.tcards{display:flex;gap:20px;margin-top:22px}
.tcard{flex:1;height:236px;background:var(--white);border-radius:6px 6px 24px 6px;text-align:center;padding:26px 60px 0}
.avatar{width:50px;height:50px;border-radius:50%;background:#cfd6e2;margin:0 auto}
.stars{color:var(--yellow);font-size:10px;letter-spacing:1px;margin-top:6px}
.tcard p{font-size:9.5px;color:var(--muted);line-height:1.55;margin-top:12px}
.tcard b{display:block;font-size:10.5px;font-weight:600;margin-top:12px}
.tcard small{font-size:9.5px;color:var(--muted)}
.arrow{position:absolute;top:50%;width:20px;height:20px}

/* blog */
.blog{height:505px;padding-top:50px;position:relative}
.posts{display:flex;gap:20px;margin-top:20px}
.post{width:312px}
.post .ph{height:184px;background:linear-gradient(150deg,#f3f4f6,#b8bec6 60%,#3a3f48)}
.date{color:var(--blue);font-size:9.5px;margin-top:12px;display:flex;gap:6px;align-items:center}
.post h3{font-size:12px;font-weight:600;margin-top:9px}
.post p{font-size:9.5px;color:var(--muted);line-height:1.5;margin-top:6px}
.post a{color:var(--blue);font-size:9.5px;display:inline-flex;gap:6px;align-items:center;margin-top:8px}

/* faq */
.faq{height:522px;background:var(--pale);padding-top:40px}
.qs{margin-top:20px}
.q{border-bottom:1px solid var(--line);padding:18px 0;display:flex;justify-content:space-between;font-size:13px;font-weight:500}
.q .a{font-size:9.5px;color:var(--muted);font-weight:400;margin-top:10px;line-height:1.55;width:560px}
.q em{font-style:normal;font-size:17px;color:var(--muted);font-weight:400;padding-right:50px}

/* contact */
.contact{height:423px;background:var(--red);padding-top:48px}
.contact .wrap{display:flex;gap:50px}
.map{width:478px;height:330px;border-radius:6px 6px 26px 6px;background:linear-gradient(135deg,#eceae3,#dcdad2)}
.form{width:415px;padding-top:42px}
.form h2{color:var(--white);font-size:27px;font-weight:600}
.field{background:var(--white);border-radius:3px;height:30px;font-size:9.5px;color:#9aa0ab;padding:0 10px;display:flex;align-items:center;margin-top:12px}
.row{display:flex;gap:12px}
.row .field{flex:1}
.field.tall{height:82px;align-items:flex-start;padding-top:10px}
.form .btn{margin-top:14px;padding:8px 32px}

/* footer */
.foot{height:310px;background:var(--blue);color:var(--white);padding-top:38px}
.fcols{display:flex}
.fcols .about{width:290px}
.fcols .about p{font-size:9.5px;line-height:1.5;margin-top:14px;width:210px}
.brand.light{color:var(--white)}
.brand.light i{background:var(--yellow)}
.fcol h4{font-size:14px;font-weight:600;margin-top:8px}
.fcol ul{list-style:none;margin-top:18px}
.fcol li{font-size:9.5px;margin-bottom:8px;line-height:1.4}
.links{width:175px}
.info{width:297px}
.info li{display:flex;gap:6px}
.info u{text-decoration:underline}
.news p{font-size:9.5px;margin-top:18px}
.sub{width:213px;height:28px;background:var(--white);border-radius:3px;margin-top:10px;display:flex;align-items:center;justify-content:space-between;padding:0 4px 0 10px;font-size:9px;color:#9aa0ab}
.sub .btn{padding:4px 10px;font-size:8.5px}
.social{display:flex;gap:10px;margin-top:14px}
.social i{width:24px;height:24px;border-radius:50%;background:var(--white);display:block}
.copy{font-size:9.5px;line-height:1.5;position:absolute;left:0;top:185px}
</style>
</head>
<body>

<header class="nav">
  <div class="wrap">
    <a class="brand" href="#"><i></i>HARBOR TIDY SQUAD</a>
    <nav class="menu">
      <a class="active" href="#">HOME</a><a href="#">ABOUT US</a><a href="#">SERVICES</a><a href="#">HOW WE WORK</a><a href="#">BLOG</a><a href="#">CONTACT</a>
      <a class="btn" href="#">LOGIN</a>
    </nav>
  </div>
</header>

<section class="hero">
  <div class="ph" role="img" aria-label="Cleaner in yellow gloves spraying a kitchen cabinet" style="position:absolute;right:0;top:0;width:520px;height:563px;background:linear-gradient(90deg,rgba(0,0,0,0),rgba(120,110,100,.35))"></div>
  <div class="wrap">
    <h1>Professional Cleaning<br>for Every Industry</h1>
    <p>From offices to medical clinics, our expert team delivers consistent results that keep your business looking its best</p>
    <div class="search">
      <span><svg width="11" height="11" viewBox="0 0 12 12"><path d="M6 11S2 7 2 4.5a4 4 0 0 1 8 0C10 7 6 11 6 11z" fill="none" stroke="#333"/><circle cx="6" cy="4.5" r="1.4" fill="none" stroke="#333"/></svg>Location</span>
      <span><svg width="11" height="11" viewBox="0 0 12 12"><circle cx="6" cy="3.5" r="2.2" fill="none" stroke="#333"/><path d="M2 11c0-3 2-4.5 4-4.5s4 1.5 4 4.5" fill="none" stroke="#333"/></svg>Service Type ⌄</span>
      <span><svg width="11" height="11" viewBox="0 0 12 12"><rect x="1.5" y="2.5" width="9" height="8" fill="none" stroke="#333"/><path d="M1.5 5h9M4 1v3M8 1v3" stroke="#333"/></svg>Date</span>
      <a class="btn" href="#">Book Now</a>
    </div>
  </div>
  <div class="stats">
    <div class="stat"><b>1000+</b><small>Happy Customers</small></div>
    <div class="stat"><b>150+</b><small>Team Members</small></div>
    <div class="stat"><b>98%</b><small>Customer Satisfaction</small></div>
    <div class="stat"><b>24 hrs</b><small>Cleaning Service Provider</small></div>
  </div>
</section>

<section class="excel">
  <div class="wrap">
    <div class="ph photo" role="img" aria-label="Two smiling cleaners in overalls giving thumbs up"></div>
    <div class="badge"><b>15+</b><small>Years<br>Experience</small></div>
    <div>
      <h2>Excellence in Every Clean</h2>
      <p>Harbor Tidy Squad has been in the commercial and industrial cleaning maintenance industry for over 15 years. The high standard of quality and extensive experience guarantees a commitment to ensure your building continually carries the prestigious look customer's demand</p>
      <ul class="ticks">
        <li><svg width="12" height="10" viewBox="0 0 12 10"><path d="M1 5l3.5 3.5L11 1" fill="none" stroke="#1b47c2" stroke-width="2"/></svg>Experience in cleaning facilities of most industries</li>
        <li><svg width="12" height="10" viewBox="0 0 12 10"><path d="M1 5l3.5 3.5L11 1" fill="none" stroke="#1b47c2" stroke-width="2"/></svg>All services are supervised and inspected on a regular basis to ensure quality</li>
        <li><svg width="12" height="10" viewBox="0 0 12 10"><path d="M1 5l3.5 3.5L11 1" fill="none" stroke="#1b47c2" stroke-width="2"/></svg>Provides a full range of cleaning services including day porter service and construction cleanup</li>
      </ul>
      <a class="btn" href="#">Learn More</a>
    </div>
  </div>
</section>

<section class="services">
  <div class="wrap">
    <h2 class="h2">Our Cleaning Services</h2>
    <p class="lead">From offices and schools to clinics and construction sites — Harbor Tidy Squad delivers reliable, high-quality cleaning tailored to every professional space</p>
    <div class="cards">
      <div class="card"><div class="ph" role="img" aria-label="Two cleaners washing office windows"></div><div class="label">Window Cleaning <svg width="36" height="8" viewBox="0 0 36 8"><path d="M0 4h34M30 1l4 3-4 3" fill="none" stroke="#1b47c2" stroke-width="1.3"/></svg></div></div>
      <div class="card feature"><div class="ph" role="img" aria-label="Cleaner wiping a table near a plant"></div>
        <div class="over"><h3>Table Cleaning</h3><p>We go beyond wiping surfaces. Our table cleaning process includes disinfecting high-touch areas, removing residue and buildup....</p><a href="#">Learn More <svg width="18" height="6" viewBox="0 0 18 6"><path d="M0 3h16M13 1l3 2-3 2" fill="none" stroke="#fff"/></svg></a></div></div>
      <div class="card"><div class="ph" role="img" aria-label="Cleaners mopping an office floor"></div><div class="label">Floor Cleaning <svg width="36" height="8" viewBox="0 0 36 8"><path d="M0 4h34M30 1l4 3-4 3" fill="none" stroke="#1b47c2" stroke-width="1.3"/></svg></div></div>
    </div>
    <div class="center"><a class="btn" href="#">View More</a></div>
  </div>
</section>

<section class="how">
  <div class="wrap">
    <h2 class="h2">How We Work</h2>
    <p class="lead">Our process is simple, transparent, and designed around your business. From the first walkthrough to the final inspection, we make sure every detail is handled with care and precision</p>
    <div class="steps">
      <svg class="dash" width="975" height="110" viewBox="0 0 975 110"><path d="M240 38 Q330 -20 420 40" fill="none" stroke="#1b47c2" stroke-dasharray="4 4"/><path d="M545 75 Q640 120 725 65" fill="none" stroke="#1b47c2" stroke-dasharray="4 4"/></svg>
      <div class="step"><div class="ring"><svg width="38" height="44" viewBox="0 0 38 44"><rect x="4" y="5" width="30" height="37" rx="3" fill="none" stroke="#1b47c2" stroke-width="1.6"/><rect x="12" y="2" width="14" height="7" rx="2" fill="#fff" stroke="#1b47c2" stroke-width="1.6"/><path d="M10 18h18M10 25h18M10 32h12" stroke="#1b47c2" stroke-width="1.6"/></svg></div><h3>Assessment &amp; Quote</h3><p>We start with a site visit or consultation to understand your cleaning needs and provide a clear, no-obligation quote</p></div>
      <div class="step"><div class="ring"><svg width="40" height="44" viewBox="0 0 40 44"><rect x="6" y="14" width="14" height="26" rx="3" fill="none" stroke="#1b47c2" stroke-width="1.6"/><path d="M9 14V8h8v6M13 8V3h8" fill="none" stroke="#1b47c2" stroke-width="1.6"/><rect x="24" y="24" width="12" height="16" rx="2" fill="none" stroke="#ee2b1f" stroke-width="1.6"/></svg></div><h3>Customized Cleaning Plan</h3><p>Every business is unique — we create a tailored cleaning schedule that fits your space, budget, and hours of operation</p></div>
      <div class="step"><div class="ring"><svg width="40" height="44" viewBox="0 0 40 44"><circle cx="18" cy="12" r="7" fill="none" stroke="#1b47c2" stroke-width="1.6"/><path d="M5 40c0-10 6-15 13-15s13 5 13 15" fill="none" stroke="#1b47c2" stroke-width="1.6"/><path d="M34 8v32" stroke="#ee2b1f" stroke-width="1.6"/></svg></div><h3>Professional Services</h3><p>Our trained crew delivers consistent, high-quality cleaning. Regular check-ins ensure your satisfaction and lasting results</p></div>
    </div>
  </div>
</section>

<section class="why">
  <div class="wrap">
    <div>
      <h2>Why Choose Us</h2>
      <p class="intro">Choosing the right cleaning company matters. At Harbor Tidy Squad, we combine skilled professionals, reliable service, and eco-friendly practices to deliver exceptional results every time</p>
      <div class="feats">
        <div class="feat"><svg width="30" height="30" viewBox="0 0 30 30"><path d="M15 3l10 4v7c0 7-5 11-10 13C10 25 5 21 5 14V7z" fill="none" stroke="#1b47c2" stroke-width="1.5"/><path d="M10 15l4 4 6-8" fill="none" stroke="#1b47c2" stroke-width="1.5"/></svg><div><b>Fully Licensed &amp; Insured</b><span>Your business is protected and<br>your property is in trusted hand</span></div></div>
        <div class="feat"><svg width="30" height="30" viewBox="0 0 30 30"><circle cx="15" cy="15" r="11" fill="none" stroke="#1b47c2" stroke-width="1.5"/><path d="M9 21c4-8 8-10 13-12" fill="none" stroke="#1b47c2" stroke-width="1.5"/></svg><div><b>Eco Friendly Products</b><span>Safe, sustainable cleaning for<br>people and the planet</span></div></div>
        <div class="feat"><svg width="30" height="30" viewBox="0 0 30 30"><circle cx="15" cy="15" r="11" fill="none" stroke="#1b47c2" stroke-width="1.5"/><path d="M15 8v7l5 3" fill="none" stroke="#1b47c2" stroke-width="1.5"/></svg><div><b>Flexible Scheduling</b><span>We work around your business<br>hours to minimize disruption</span></div></div>
        <div class="feat"><svg width="30" height="30" viewBox="0 0 30 30"><circle cx="12" cy="9" r="5" fill="none" stroke="#1b47c2" stroke-width="1.5"/><path d="M3 27c0-7 4-11 9-11s9 4 9 11" fill="none" stroke="#1b47c2" stroke-width="1.5"/><path d="M21 14l2 2 4-5" fill="none" stroke="#1b47c2" stroke-width="1.5"/></svg><div><b>Trained &amp; Screened Staff</b><span>Professionally trained cleaners for<br>consistent, high-quality results</span></div></div>
      </div>
    </div>
    <div class="ph photo" role="img" aria-label="Masked cleaner spraying a glass window"></div>
  </div>
</section>

<section class="testi">
  <svg class="arrow" style="left:85px" viewBox="0 0 20 20"><path d="M13 3L6 10l7 7" fill="none" stroke="#fff" stroke-width="2"/></svg>
  <svg class="arrow" style="right:85px" viewBox="0 0 20 20"><path d="M7 3l7 7-7 7" fill="none" stroke="#fff" stroke-width="2"/></svg>
  <div class="wrap">
    <h2 class="h2">Testimonials</h2>
    <div class="tcards">
      <div class="tcard"><div class="avatar" role="img" aria-label="Customer portrait"></div><div class="stars">★★★★★</div><p>Their crew is fantastic — always on time, friendly, and efficient. What I appreciate most is how proactive they are in communicating and ensuring every task is done right. You can tell they truly care about their work</p><b>Marcus T.</b><small>Property Manager</small></div>
      <div class="tcard"><div class="avatar" role="img" aria-label="Customer portrait"></div><div class="stars">★★★★★</div><p>We operate a large medical facility, and cleanliness is critical. Harbor Tidy Squad maintains the highest standards — they're detail-oriented, responsive, and professional. We've had nothing but positive experiences with their team</p><b>Elena V.</b><small>Office Manager</small></div>
    </div>
  </div>
</section>

<section class="blog">
  <svg class="arrow" style="left:85px;top:250px" viewBox="0 0 20 20"><path d="M13 3L6 10l7 7" fill="none" stroke="#1b47c2" stroke-width="2"/></svg>
  <svg class="arrow" style="right:85px;top:250px" viewBox="0 0 20 20"><path d="M7 3l7 7-7 7" fill="none" stroke="#1b47c2" stroke-width="2"/></svg>
  <div class="wrap">
    <h2 class="h2">Latest Blog</h2>
    <p class="lead">Discover our newest cleaning solutions designed to meet the needs of modern businesses. From deep cleaning to specialty care, we keep every space spotless, safe, and ready for work</p>
    <div class="posts">
      <div class="post"><div class="ph" role="img" aria-label="Cleaners tidying an office workspace"></div><div class="date"><svg width="10" height="10" viewBox="0 0 12 12"><rect x="1.5" y="2.5" width="9" height="8" fill="none" stroke="#1b47c2"/><path d="M1.5 5h9" stroke="#1b47c2"/></svg>June 21, 2025</div><h3>Expert Tips and Industry Updates</h3><p>We share expert advice, cleaning hacks, and company updates to help you maintain a spotless, healthy....</p><a href="#">Learn More →</a></div>
      <div class="post"><div class="ph" role="img" aria-label="Cleaner wiping a desk in an office"></div><div class="date"><svg width="10" height="10" viewBox="0 0 12 12"><rect x="1.5" y="2.5" width="9" height="8" fill="none" stroke="#1b47c2"/><path d="M1.5 5h9" stroke="#1b47c2"/></svg>June 22, 2025</div><h3>The Power of Professional Care</h3><p>Hiring trained cleaning professionals saves time and ensures consistent results. Learn how Harbor....</p><a href="#">Learn More →</a></div>
      <div class="post"><div class="ph" role="img" aria-label="Masked cleaner disinfecting a bright room"></div><div class="date"><svg width="10" height="10" viewBox="0 0 12 12"><rect x="1.5" y="2.5" width="9" height="8" fill="none" stroke="#1b47c2"/><path d="M1.5 5h9" stroke="#1b47c2"/></svg>June 23, 2025</div><h3>A Higher Standard of Hygiene</h3><p>Shared spaces demand more attention than ever. From doorknobs to desks, our disinfection practices....</p><a href="#">Learn More →</a></div>
    </div>
  </div>
</section>

<section class="faq">
  <div class="wrap">
    <h2 class="h2">Frequently Asked Questions</h2>
    <div class="qs">
      <div class="q"><span>Can you handle large commercial or multi-site contracts?</span><em>+</em></div>
      <div class="q"><div>Do you offer one-time cleaning or only regular contracts?<div class="a">We offer both! Whether you need a one-time deep clean or a customized ongoing maintenance plan, we'll design a program that fits your facility's needs and schedule</div></div><em>−</em></div>
      <div class="q"><span>Do you provide custom cleaning plans?</span><em>+</em></div>
      <div class="q"><span>Do you bring your own cleaning supplies and equipment?</span><em>+</em></div>
      <div class="q"><span>Do you offer disinfection or sanitization services?</span><em>+</em></div>
    </div>
    <div class="center"><a class="btn" href="#">See All FAQs</a></div>
  </div>
</section>

<section class="contact">
  <div class="wrap">
    <div class="ph map" role="img" aria-label="Street map showing the office location"></div>
    <div class="form">
      <h2>Contact Us</h2>
      <div class="field">Enter your name</div>
      <div class="row"><div class="field">Enter your email</div><div class="field">Your mobile number</div></div>
      <div class="field tall">Message....</div>
      <a class="btn" href="#">Send</a>
    </div>
  </div>
</section>

<footer class="foot">
  <div class="wrap">
    <div class="fcols">
      <div class="about"><a class="brand light" href="#"><i></i>HARBOR TIDY SQUAD</a><p>At Harbor Tidy Squad, we take pride in keeping your workplace clean, healthy, and welcoming. From offices to large facilities, our team delivers quality you can see and service you can trust</p></div>
      <div class="fcol links"><h4>Quick links</h4><ul><li>Home</li><li>About Us</li><li>Services</li><li>Why Choose Us</li><li>How We Work</li><li>Contact</li></ul></div>
      <div class="fcol info"><h4>Contact</h4><ul>
        <li><span>⌖</span><span>Harbor Tidy Squad<br>418 Larkfield Ave Ste B<br>Marlow Bay, Ca 90000</span></li>
        <li><span>✆</span><span><b>Toll Free:</b> 800-555-0142<br><b>Fax:</b> 555-010-3377</span></li>
        <li><span>✉</span><span><b>Email:</b> <u>info@harbortidy.test</u><br><b>Service:</b> <u>service@harbortidy.test</u><br><b>Billing:</b> <u>billing@harbortidy.test</u><br><b>Quotes:</b> <u>quotes@harbortidy.test</u><br><b>Subcontracting:</b> <u>partners@harbortidy.test</u></span></li>
      </ul></div>
      <div class="fcol news"><h4>Newsletter</h4><p>Sign up and subscribe our Newsletter</p><div class="sub">Enter your email<span class="btn">Subscribe</span></div><div class="social"><i></i><i></i><i></i><i></i></div></div>
    </div>
    <p class="copy">Copyrights © 2025 Harbor Tidy Squad<br>A Full Service Commercial Cleaning Company.</p>
  </div>
</footer>

</body>
</html>
```